Craft Brewery Beer Can Label in Alaska

Design a 16oz can label for a craft brewery.

We are making a can design that can be used for our 6 normal beers. Our desire is to have a standard design but one major element have the color change on each beer type. We included examples of how this works for others.

Elements we general like in designs - mountain scenes, waterfalls, topo map lines, hops. None/all are not required in a design but gives starting options. We are on the ocean in a glacier fjord so think mountains, glaciers and water.

Requirements
Must have
• Company Logo – provided
Forged by Frontier Logo – provided
Sovereign Maltsters Logo – provided

Alcohol warning text -

GOVERNMENT WARNING: (1) According to the Surgeon General, women should not drink alcoholic beverages during pregnancy because of the risk of birth defects. (2) Consumption of alcoholic beverages impairs your ability to drive a car or operate machinery, and may cause health problems.

Beer Name – Tide Mark Pilsner
ABV – 4.9% ABV
Size – 16 FL OZ
Nice to have
• Elements we general like in designs - mountain scenes, waterfalls, topo map lines, hops. None/all are not required in a design but gives starting options. We are on the ocean in a glacier fjord so think mountains, glaciers and water.

```html
<!DOCTYPE html>
<html lang="en">
<head>
<meta charset="utf-8">
<title>Tide Mark Pilsner – Can Label</title>
<link href="https://fonts.googleapis.com/css2?family=Alfa+Slab+One&family=Oswald:wght@400;600&display=swap" rel="stylesheet">
<style>
  :root {
    --night: #0e1122;
    --cream: #f4f0dc;
    --signal-red: #d8403a;
    --ember: #b32a2a;
    --maroon: #7a1f22;
    --deep-maroon: #5e1619;
    --snow: #efe9cf;
  }
  * { margin: 0; padding: 0; box-sizing: border-box; }
  html, body { width: 1200px; height: 812px; overflow: hidden; background: var(--night); }
  .canvas { position: relative; width: 1200px; height: 812px; background: var(--night); }

  .label {
    position: absolute; left: 100px; top: 116px; width: 1000px; height: 580px;
    background: var(--maroon); overflow: hidden;
  }
  .band { position: absolute; left: 0; width: 100%; background: var(--cream); }
  .band--top { top: 0; height: 46px; }
  .band--bottom { bottom: 0; height: 40px; }

  .mountain-art {
    position: absolute; left: 0; top: 46px; width: 100%; height: 300px;
    background:
      radial-gradient(ellipse 34% 40% at 50% 42%, rgba(239,233,207,0.55) 0%, rgba(239,233,207,0) 100%),
      linear-gradient(180deg, var(--signal-red) 0%, var(--ember) 55%, var(--maroon) 100%);
  }

  .beer-name {
    position: absolute; left: 60px; top: 70px; width: 880px; text-align: center;
    font-family: "Alfa Slab One", serif; font-size: 68px; line-height: 1.0;
    color: var(--signal-red); -webkit-text-stroke: 2px var(--cream);
    text-transform: uppercase; letter-spacing: 1px;
  }

  .brand-seal {
    position: absolute; left: 410px; top: 226px; width: 180px; height: 180px;
    border-radius: 50%; background: var(--cream);
    border: 12px solid var(--snow);
    box-shadow: 0 0 0 4px var(--deep-maroon);
    display: flex; align-items: center; justify-content: center; text-align: center;
  }
  .brand-name {
    font-family: "Oswald", sans-serif; font-weight: 600; font-size: 22px; line-height: 1.15;
    color: var(--maroon); text-transform: uppercase; letter-spacing: 2px;
  }

  .abv {
    position: absolute; left: 0; top: 414px; width: 100%; text-align: center;
    font-family: "Oswald", sans-serif; font-weight: 600; font-size: 44px; line-height: 1.1;
    color: var(--cream); letter-spacing: 1px;
  }

  .warning {
    position: absolute; left: 220px; top: 472px; width: 560px;
    font-family: "Oswald", sans-serif; font-weight: 400; font-size: 12.5px; line-height: 1.35;
    color: var(--cream); text-align: center;
  }

  .volume {
    position: absolute; left: 56px; top: 482px;
    font-family: "Oswald", sans-serif; font-weight: 600; font-size: 30px; line-height: 1;
    color: var(--cream);
  }

  .partner-badge {
    position: absolute; right: 70px; top: 462px; width: 54px; height: 64px;
    background: var(--cream); border-radius: 4px;
  }
</style>
</head>
<body>
  <main class="canvas">
    <section class="label">
      <div class="band band--top"></div>
      <div class="mountain-art" role="img" aria-label="Jagged snow-capped glacier peaks illustration in red, maroon and cream"></div>
      <h1 class="beer-name">Tide Mark<br>Pilsner</h1>

      <div class="brand-seal">
        <span class="brand-name">Harbor Ridge<br>Brewing</span>
      </div>

      <p class="abv">4.9% ABV</p>

      <p class="warning">GOVERNMENT WARNING: (1) According to the Surgeon General, women should not drink alcoholic beverages during pregnancy because of the risk of birth defects. (2) Consumption of alcoholic beverages impairs your ability to drive a car or operate machinery, and may cause health problems.</p>

      <p class="volume">16 FL OZ</p>
      <div class="partner-badge" role="img" aria-label="Sovereign Maltsters partner badge"></div>

      <div class="band band--bottom"></div>
    </section>
  </main>
</body>
</html>
```